TKL Accounting Firm Needs Graphic Art for Our Proven Processes and For Our Core Values

**Looking for redesign of attached Powerpoint content (see below)
***Final graphic should be good for web use

Date: March 10, 2017

From: Curtis Alvarado, CPA
Tolbert, Kinsley & Associates, P.C. (TKL)

Background:

TKL is a 20 person Houston based CPA firm, providing tax, accounting, financial and consulting services, to individuals and to entrepreneurs and their businesses. TKL is engaged in a process called BTF (See the book Momentum, by Lars Pendleton) whereby we implement a “system” to operate our company. As part of this system we have defined what we call our “Proven Process”. This is something we will show all prospective clients, and have on our website, that explains what it looks like to work with us. Starting at the beginning of the project to completion.

Project Description:

TKL is looking for graphic artist assistance in designing the following pieces:

1. Graphic depiction of “The TKL Way”, otherwise known as our “Proven Process”. The first attachments labeled TKL will show what we have done ourselves. These will show the general steps we have defined in both a sort of graphic way and a step by step narrative. The second attachment shows you some actual examples other firms have put together, hopefully that will show you what we are asking you to develop for us. Note that we are very open to any suggested clarifications or improvements to what we have done which may include changing phrases or saying something in a different way. Remember we are accountants!

2. We have defined our core values as a company, and we are wanting to develop some posters/placards so we can post them in our conference rooms, break room, etc. Attached are our core values as well as some deeper narratives about what they mean. Also included are many of the “words” we kicked around before arriving at our core values.

3. You will also find an attachment with our logo that should be incorporated, as well. Designs SHOULD INCLUDE, but not be limited to, the colors on our logo. Our end product should reflect a strong sense of our core values.

We would like to have the project in a form that would give us the option to use any/all of the information on our website, posters, brochures, etc.

Thanks in advance for your assistance.

Project Deadline Extended Reason: We are in the midst of tax deadlines so need a little more time to review and respond. Added Monday, March 20, 2017

Target Market(s)

Entrepreneurs and their companies with revenue greater than one million; Industries such as real estate, construction, trades and professional services; all in the Greater Houston Texas area

Industry/Entity Type

Accounting

Font styles to use
Serif
Other font styles liked:
• We are okay with Serif but are open.

Requirements
Must have
• Proven Process must be presented in a way that is clear and makes sense.
Nice to have
• Clean lines
• Colors should go with logo (see attached)
Should not have
• Can't think of anything - unless I see it

```html
<!DOCTYPE html>
<html lang="en">
<head>
<meta charset="utf-8">
<title>The TKL Way – Our Proven Process</title>
<link href="https://fonts.googleapis.com/css2?family=EB+Garamond:wght@500;600;700&family=Open+Sans:wght@700;800&display=swap" rel="stylesheet">
<style>
  :root {
    --olive: #5b5a2b;
    --olive-dark: #4f4e24;
    --gold: #a98a3d;
    --gold-light: #c9ab5e;
    --paper: #ffffff;
  }
  * { margin: 0; padding: 0; box-sizing: border-box; }
  html, body { width: 1200px; height: 927px; overflow: hidden; background: var(--paper); }
  .canvas { position: relative; width: 1200px; height: 927px; overflow: hidden; background: var(--paper); }

  .page-title {
    position: absolute; left: 72px; top: 62px;
    font-family: "Open Sans", Arial, sans-serif; font-weight: 800;
    font-size: 58px; letter-spacing: 1px; color: var(--olive); line-height: 1;
  }
  .title-rule {
    position: absolute; left: 73px; top: 137px; width: 440px; height: 2px;
    background: linear-gradient(to right, var(--gold), rgba(169,138,61,0));
  }
  .page-subtitle {
    position: absolute; left: 73px; top: 152px;
    font-family: "EB Garamond", Georgia, serif; font-weight: 500;
    font-size: 40px; color: var(--gold); line-height: 1.1;
  }

  .step {
    position: absolute; width: 510px; height: 73px;
    border-left: 2px solid var(--gold);
    background:
      linear-gradient(to right, var(--gold) 0%, var(--gold) 45%, rgba(169,138,61,0) 100%) top left / 100% 2px no-repeat,
      linear-gradient(to right, var(--gold) 0%, var(--gold) 45%, rgba(169,138,61,0) 100%) bottom left / 100% 2px no-repeat;
  }
  .step-name {
    position: absolute; left: 4px; top: 0; width: 178px; height: 100%;
    display: flex; align-items: center; justify-content: center; text-align: center;
    font-family: "EB Garamond", Georgia, serif; font-weight: 700;
    font-size: 21px; line-height: 1.2; color: var(--olive-dark);
  }
  .step-detail {
    position: absolute; left: 173px; top: 0; height: 100%;
    display: flex; align-items: center;
    font-family: "Open Sans", Arial, sans-serif; font-weight: 700;
    font-size: 15px; line-height: 1.35; color: var(--gold);
  }
  .step-detail::before { content: "•"; margin-right: 6px; align-self: flex-start; padding-top: 0; }
  .step-detail span { display: block; }

  .connectors { position: absolute; left: 0; top: 0; }

  .firm-mark {
    position: absolute; left: 872px; top: 744px; width: 106px; height: 48px;
    display: flex; align-items: center; justify-content: center;
    font-family: "EB Garamond", Georgia, serif; font-weight: 600;
    font-size: 38px; color: var(--olive); letter-spacing: 1px;
  }
  .firm-name {
    position: absolute; left: 716px; top: 797px; width: 416px; text-align: center;
    font-family: "EB Garamond", Georgia, serif; font-weight: 500;
    font-size: 26px; color: var(--olive); white-space: nowrap;
  }
  .firm-rule {
    position: absolute; left: 720px; top: 832px; width: 408px; height: 1px; background: var(--olive);
  }
  .firm-tagline {
    position: absolute; left: 716px; top: 838px; width: 416px; text-align: center;
    font-family: "EB Garamond", Georgia, serif; font-weight: 600;
    font-size: 15px; letter-spacing: 8px; color: var(--gold);
  }
  .base-band {
    position: absolute; left: 0; bottom: 0; width: 1200px; height: 20px;
    background: linear-gradient(to right, var(--gold-light), var(--gold) 50%, var(--olive));
  }
</style>
</head>
<body>
<main class="canvas">
  <h1 class="page-title">THE TKL WAY</h1>
  <div class="title-rule"></div>
  <p class="page-subtitle">Our Proven Process</p>

  <svg class="connectors" width="1200" height="927" viewBox="0 0 1200 927" aria-hidden="true">
    <g fill="none" stroke="#5b5a2b" stroke-width="2.5">
      <polyline points="115,780 115,729 145,729"/>
      <polyline points="199,684 199,633 229,633"/>
      <polyline points="283,588 283,537 313,537"/>
      <polyline points="367,492 367,441 396,441"/>
      <polyline points="450,396 450,344 480,344"/>
      <polyline points="534,299 534,248 564,248"/>
      <polyline points="618,203 618,152 648,152"/>
    </g>
    <g fill="#5b5a2b">
      <polygon points="153,729 143,723 143,735"/>
      <polygon points="237,633 227,627 227,639"/>
      <polygon points="321,537 311,531 311,543"/>
      <polygon points="404,441 394,435 394,447"/>
      <polygon points="488,344 478,338 478,350"/>
      <polygon points="572,248 562,242 562,254"/>
      <polygon points="656,152 646,146 646,158"/>
    </g>
  </svg>

  <section class="steps">
    <div class="step" style="left:73px; top:780px;">
      <div class="step-name">Philosophical<br>match</div>
      <div class="step-detail"><span>Initial meeting</span></div>
    </div>
    <div class="step" style="left:157px; top:684px;">
      <div class="step-name">Set<br>Expectatiaons</div>
      <div class="step-detail"><span>Engagement letter</span></div>
    </div>
    <div class="step" style="left:241px; top:588px;">
      <div class="step-name">Determine<br>your needs</div>
      <div class="step-detail"><span>Client onboarding<br>questionnaire</span></div>
    </div>
    <div class="step" style="left:325px; top:492px;">
      <div class="step-name">Assign client<br>service staff</div>
      <div class="step-detail"><span>Personal contact<br>within 48 hours</span></div>
    </div>
    <div class="step" style="left:408px; top:396px;">
      <div class="step-name">Deeper dive into<br>your situation</div>
      <div class="step-detail"><span>Request<br>additional data</span></div>
    </div>
    <div class="step" style="left:492px; top:299px;">
      <div class="step-name">Prepare draft<br>deliverable</div>
      <div class="step-detail"><span>For tax returns, turnaround is<br>generally 10 business days</span></div>
    </div>
    <div class="step" style="left:576px; top:203px;">
      <div class="step-name">Execute final<br>deliverable</div>
      <div class="step-detail"><span>File tax return</span></div>
    </div>
    <div class="step" style="left:660px; top:107px;">
      <div class="step-name">Complete<br>feedback loop</div>
      <div class="step-detail"><span>Were your expectations met?<br>How can we improve?</span></div>
    </div>
  </section>

  <footer>
    <div class="firm-mark">TKL</div>
    <div class="firm-name">Tolbert, Kinsley &amp; Associates, PC</div>
    <div class="firm-rule"></div>
    <div class="firm-tagline">CPAs &amp; Advisors</div>
  </footer>

  <div class="base-band"></div>
</main>
</body>
</html>
```